Seriöser Briefkopf für Rechtsanwaltskanzlei
Zielgruppe
Rechtsanwaltskanzlei
Aufgabenstellung
Benötigt wird ein seriöser Briefkopf für eine Anwaltskanzlei. Er soll im Wesentlichen aus Typen bestehen, mit denen aber durchaus 'gespielt' werden soll (Groß- und Kleinschreibung, querstehend, angeschnitten o.Ä)
Folgender Inhalt muss untergebracht werden:
Rechtsanwaltskanzlei Kessenhagen
Rechtsanwalt Dipl.-Ing. Udo Kessenhagen
Rechtsanwalt Matthias Wendel
Der Briefkopf muss schwarz-weiß druckbar sein und beim Versenden per Fax müssen alle Daten gut lesbar bleiben (also keine Grautöne bei Tel-Nr. o.Ä.)
Der Briefkopf soll mit einem Drucker ausgedruckt werden, sodass keine Gestaltung bis zum Blattrand gehen darf.
Bitte keine Logos mit Paragrafen-Zeichen oder Justitia und nicht die Abkürzung RUK verwenden.
Keine - Einfach drauflos - Ich bin gespannt

```html
<!DOCTYPE html>
<html lang="de">
<head>
<meta charset="utf-8">
<title>Briefkopf Rechtsanwaltskanzlei Kessenhagen</title>
<link rel="stylesheet" href="https://fonts.googleapis.com/css2?family=EB+Garamond:wght@400&display=swap">
<style>
  :root {
    --paper: #ffffff;
    --ink: #111111;
    --rule: #333333;
  }
  html, body {
    margin: 0;
    padding: 0;
    width: 849px;
    height: 1200px;
    overflow: hidden;
    background: var(--paper);
  }
  .letterhead {
    position: relative;
    width: 849px;
    height: 1200px;
    background: var(--paper);
    color: var(--ink);
    font-family: "EB Garamond", Georgia, serif;
    font-weight: 400;
  }
  .firm-name {
    position: absolute;
    right: 52px;
    top: 52px;
    margin: 0;
    text-align: right;
    font-weight: 400;
    color: var(--ink);
    line-height: 1;
  }
  .firm-name .firm-type {
    display: block;
    font-size: 18px;
    letter-spacing: 1.6px;
  }
  .firm-name .firm-surname {
    display: block;
    margin-top: 4px;
    font-size: 23px;
    letter-spacing: 2.4px;
    text-transform: uppercase;
  }
  .frame {
    position: absolute;
    top: 0;
    left: 0;
  }
  .sender {
    position: absolute;
    left: 591px;
    top: 112px;
    font-size: 11.6px;
    line-height: 12.8px;
  }
  .sender p {
    margin: 0;
  }
  .sender .partners { margin-bottom: 27px; }
  .sender .address,
  .sender .phone { margin-bottom: 8px; }
  .sender .label {
    display: inline-block;
    width: 23px;
  }
</style>
</head>
<body>
<div class="letterhead">
  <h1 class="firm-name">
    <span class="firm-type">Rechtsanwaltskanzlei</span>
    <span class="firm-surname">Kessenhagen</span>
  </h1>

  <svg class="frame" width="849" height="1200" viewBox="0 0 849 1200" aria-hidden="true">
    <g stroke="var(--rule)" stroke-width="0.8" fill="none">
      <line class="head-rule" x1="70" y1="105.5" x2="801.5" y2="105.5"/>
      <line class="side-rule" x1="801.5" y1="105.5" x2="801.5" y2="1145.5"/>
      <line class="foot-rule" x1="591" y1="1145.5" x2="801.5" y2="1145.5"/>
      <line class="fold-mark" x1="12" y1="416" x2="28" y2="416"/>
      <line class="fold-mark" x1="12" y1="832" x2="28" y2="832"/>
    </g>
  </svg>

  <address class="sender" style="font-style:normal">
    <p class="partners">Rechtsanwalt Dipl.-Ing. Udo Kessenhagen<br>Rechtsanwalt Matthias Wendel</p>
    <p class="address">Gerberweg 7<br>04109 Leipzig</p>
    <p class="phone"><span class="label">Tel.</span> 0341 58213-0<br><span class="label">Fax</span> 0341 58213-46</p>
    <p class="online">mail@kessenhagen-kanzlei.de<br>www.kessenhagen-kanzlei.de</p>
  </address>
</div>
</body>
</html>
```